Amber Tides: Lantern Tales from Seven Winters by the Northern Sea and Other Small Wonders

Good day! I am excited to work again with you, amazing designers! This time I am looking for the cover design of my book.
Dimensions 6” x 9”
The book name is as my name project. I love simplicity, but yet that is impactful. I love colours, I don't have a specific colour in mind, but I like the mustard colour as the one in the logo of my company. I am open to ideas! I have attached some cover samples that I like so that it gives a better idea of what I have on mind.
I am looking for something that looks professional, yet, not super serious, that it's approachable to people. Something that calls their attention at first glance.
I am working with my editor and my interior designer as well to finalize this part of the book. I will be working with the person that I select for the book design to finalize it.
About the book, here a passage of an unedited version of the introduction for guidance :
My intention is to take you on a journey to help you to understand what is going on in your mind so that you get out from anything that is holding you back in your life. My intention is to guide you to start fully living and experiencing a life that your mind even have yet conceived. To experience a life where you live fearless and without suffering. Living your life where you are the navigator and the creator of how you are experiencing it and you are living in a world of possibilities where there are no limitations.
For it, we will start to understand more about the mind and about the brain. I am not a neuroscientist and neither I consider my self an expert in the workings of the brain, what I know is the result of my fascination about our brain. This curiosity and the part of me that likes to understand how things work took me to read, research and learn about how our brain works and how its intrinsic mechanisms are subconsciously influencing and limiting us. I encourage you to stay on this part, it can be a bit technical, but understanding how it works will empower you not to allow your mind to dictate the way you approach your life and to live on autopilot.
We will continue to describe how you have been programmed throughout your life, putting you inside a box limited by your subconscious beliefs and ideas about the world. In this part, we will also discuss what ego is, how it is subconsciously limiting you and how the ways of when ego manifests itself are limiting you and making you suffer. Now that you know how you have been enclosed in your mind for all your life, we will move to discuss how you can get out of it. You will learn how to master your emotions to eliminate your suffering and not allow them to control the direction of your life and use them as a mechanism to get out from your programed mind. We continue to discuss how to leverage the power of your mind and harness your power of choice. Finally, I invite you to see yourself as a holistic being so that you start truly living and take control over the direction of your life, by nourishing and taking care of all those aspects of you utilizing their wisdom and synergy to achieve higher connection within yourself, your soul and live your life in a higher level of consciousness with peace, flow, love and purpose.

```html
<!DOCTYPE html>
<html lang="en">
<head>
<meta charset="utf-8">
<title>Amber Tides – Book Cover</title>
<link href="https://fonts.googleapis.com/css2?family=Libre+Baskerville:wght@700&family=Poppins:wght@600&display=swap" rel="stylesheet">
<style>
  :root {
    --backdrop: #121112;
    --navy-top: #0b3465;
    --sky-bottom: #4787cf;
    --mustard: #fdc216;
    --butter: #f2dd86;
    --ink-blue: #2a5c9e;
  }
  html, body {
    margin: 0;
    padding: 0;
    width: 843px;
    height: 1200px;
    overflow: hidden;
    background: var(--backdrop);
  }
  .cover {
    position: absolute;
    left: 100px;
    top: 111px;
    width: 668px;
    height: 991px;
    display: block;
  }
  .title-display {
    font-family: "Libre Baskerville", Georgia, serif;
    font-weight: 700;
    fill: var(--mustard);
  }
  .banner-text {
    font-family: "Poppins", "Century Gothic", sans-serif;
    font-weight: 600;
    fill: var(--ink-blue);
    text-anchor: middle;
  }
  .author {
    font-family: "Poppins", "Century Gothic", sans-serif;
    font-weight: 600;
    fill: var(--mustard);
    text-anchor: middle;
    letter-spacing: 2px;
  }
</style>
</head>
<body>
<svg class="cover" viewBox="0 0 668 991" xmlns="http://www.w3.org/2000/svg" aria-label="Book cover: Amber Tides">
  <defs>
    <linearGradient id="cover-sky" x1="0" y1="0" x2="0" y2="1">
      <stop offset="0" stop-color="var(--navy-top)"/>
      <stop offset="1" stop-color="var(--sky-bottom)"/>
    </linearGradient>
  </defs>

  <rect class="cover-field" x="0" y="0" width="668" height="991" fill="url(#cover-sky)"/>

  <text class="title-display" x="52" y="261" font-size="165" textLength="530" lengthAdjust="spacingAndGlyphs">AMBER</text>
  <text class="title-display" x="108" y="417" font-size="165" textLength="290" lengthAdjust="spacingAndGlyphs">TIDES</text>

  <rect class="emblem-placeholder" x="410" y="284" width="108" height="148" fill="var(--mustard)" role="img" aria-label="Illustration area: light bulb emblem"/>

  <polygon class="banner banner-primary" points="22,431 646,447 632,527 37,499" fill="var(--mustard)"/>
  <text class="banner-text" x="334" y="497" font-size="35">LANTERN TALES FROM</text>

  <polygon class="banner banner-soft" points="81,535 485,535 458,664 90,660" fill="var(--butter)"/>
  <text class="banner-text" x="278" y="588" font-size="31">SEVEN WINTERS BY</text>
  <text class="banner-text" x="276" y="645" font-size="31">THE NORTHERN SEA</text>

  <polygon class="banner banner-and" points="469,565 585,568 583,647 463,643" fill="var(--mustard)"/>
  <text class="banner-text" x="525" y="621" font-size="34">AND</text>

  <polygon class="banner banner-primary" points="65,675 570,675 596,815 88,783" fill="var(--mustard)"/>
  <text class="banner-text" x="334" y="721" font-size="38">OTHER SMALL</text>
  <text class="banner-text" x="334" y="781" font-size="38">WONDERS</text>

  <text class="author" x="334" y="929" font-size="44">MARA LINDQVIST</text>
</svg>
</body>
</html>
```